Asia based real estate financing firm needs and AWESOME design for a biz card -Harbor Lending Circle

Looking for a stylish, & corporate-looking business card for a real estate financing brokerage firm in Asia, offering global mortgage loans. I uploaded our current logos. We would like to add a splash of color (perhaps the house icon) or any other suggestions are open. For the winning designer, we have a lot of work! Thanks and best of luck!

Target Market(s)

Real estate investors globally. We want to look more like a BANK and NOT a real estate company. Please don't play up on a "house" design.

Industry/Entity Type

Banking

Contact Information for Business Card

Harbor Lending Circle
Peter Wilks
Co-Founder | Partner

14 Cassia Lane, Suite 310
Singapore 047219
www.hlc-example.asia
peterwilks@hlc-example.asia
+65 555-0142
WeChat: peterwilks

Colors

Designer to choose colors to be used in the design.

Requirements
Must have
• Must have the standard business requirements for a card; name, address, email, etc
• Can be horizontal or vertical.
Nice to have
• It would be great to see some sort of variation to the logo with a pop of color. Red is good as we're in Asia, however, other options work as well.
• Our tag line is - Borderless mortgages. It doesn't have to be on the card but might be nice.
• I'd like to start seeing our tagline within the cards as well. - Borderless mortgages.
• Also, please add our location. The location for this card is Singapore so perhaps it can be highlighted or emphasised in some way.
• Singapore | Hong Kong | Shanghai | Manila
• As we will soon open an office in Shanghai, having an option for both languages would be great.
Should not have
• I'm exceited and open to your creativity ... knock it out of the park!

```html
<!DOCTYPE html>
<html lang="en">
<head>
<meta charset="utf-8">
<title>Harbor Lending Circle — Business Card</title>
<link href="https://fonts.googleapis.com/css2?family=Arimo:ital,wght@0,400;0,700;1,400;1,700&display=swap" rel="stylesheet">
<style>
  :root {
    --page: #fbfbfb;
    --red: #c01f25;
    --red-bright: #e32028;
    --blue: #2a5aab;
    --blue-band: #2d58a8;
    --navy: #141d5a;
    --black: #0b0b0b;
    --white: #ffffff;
    --ink: #151515;
    --handle-dot: #9aa3b5;
  }
  * { box-sizing: border-box; margin: 0; padding: 0; }
  html, body { width: 1200px; height: 826px; overflow: hidden; background: var(--page); }
  body { position: relative; font-family: "Arimo", Arial, sans-serif; }

  .card { position: absolute; top: 193px; width: 264px; height: 462px; overflow: hidden; }
  .card--front { left: 266px; }
  .card--back { left: 642px; }
  .card__bg { position: absolute; inset: 0; width: 264px; height: 462px; }

  .brand { position: absolute; left: 22px; right: 0; top: 70px; text-align: center; }
  .card--back .brand { left: 26px; }
  .brand__mark { display: block; width: 12px; height: 12px; margin: 0 auto 22px; background: var(--red); }
  .brand__name { display: block; font-weight: 700; font-size: 21px; line-height: 1; color: var(--red); white-space: nowrap; }

  .tagline { position: absolute; left: 41px; top: 183px; font-style: italic; font-size: 19.5px; line-height: 1; color: var(--white); }
  .cities--front { position: absolute; left: 41px; top: 223px; font-weight: 700; font-size: 9.5px; line-height: 1; color: var(--red-bright); white-space: nowrap; }
  .region-map {
    position: absolute; left: 40px; top: 240px; width: 210px; height: 150px;
    background: radial-gradient(ellipse at 55% 50%, rgba(42,95,196,0.55) 0%, rgba(42,95,196,0.18) 55%, rgba(42,95,196,0) 80%);
  }

  .person__name { position: absolute; left: 38px; top: 177px; font-weight: 700; font-size: 19px; line-height: 1; color: var(--white); }
  .person__title { position: absolute; left: 102px; top: 222px; font-weight: 700; font-style: italic; font-size: 15px; line-height: 1; color: var(--white); white-space: nowrap; }

  .contact { position: absolute; left: 66px; font-style: italic; font-size: 10px; color: var(--ink); line-height: 1.1; white-space: nowrap; }
  .contact--phone { top: 256px; font-weight: 700; font-size: 11.5px; }
  .contact--email { top: 290px; }
  .contact--web { top: 324px; }
  .contact--address { top: 350px; font-size: 9.5px; }

  .icon { position: absolute; left: 26px; width: 22px; height: 22px; }
  .icon--phone { top: 249px; }
  .icon--email { top: 284px; }
  .icon--web { top: 318px; }
  .icon--pin { top: 350px; }

  .handle { position: absolute; left: 208px; top: 306px; width: 54px; text-align: center; }
  .handle__dot { display: block; width: 14px; height: 14px; border-radius: 50%; background: var(--handle-dot); margin: 0 auto 4px; }
  .handle__id { font-weight: 700; font-style: italic; font-size: 9.5px; color: var(--ink); }

  .cities--back { position: absolute; left: 36px; top: 393px; font-size: 9.5px; line-height: 1; color: var(--ink); white-space: nowrap; }
</style>
</head>
<body>

<section class="card card--front" aria-label="Card front">
  <svg class="card__bg" viewBox="0 0 264 462" aria-hidden="true">
    <defs>
      <linearGradient id="navyFill" x1="0" y1="0" x2="0" y2="1">
        <stop offset="0" stop-color="#1a2a78"/>
        <stop offset="1" stop-color="#0f1748"/>
      </linearGradient>
    </defs>
    <rect width="264" height="462" fill="var(--red)"/>
    <path d="M0,92 C70,40 180,18 264,48 L264,400 C180,425 80,420 0,395 Z" fill="var(--blue)"/>
    <path d="M22,96 C90,70 190,62 264,86 L264,400 C180,420 90,418 22,402 Z" fill="var(--white)"/>
    <rect x="22" y="171" width="242" height="42" fill="var(--blue-band)"/>
    <path d="M22,213 L264,213 L264,392 C180,412 90,412 22,396 Z" fill="url(#navyFill)"/>
    <path d="M0,84 L22,96 L22,402 L0,395 Z" fill="var(--black)"/>
    <path d="M0,398 C80,418 180,420 264,398 L264,412 C180,432 80,432 0,412 Z" fill="var(--blue)" stroke="var(--white)" stroke-width="2"/>
    <path d="M0,414 C80,434 180,434 264,414 L264,462 L0,462 Z" fill="var(--red)"/>
  </svg>

  <div class="brand">
    <span class="brand__mark"></span>
    <span class="brand__name">Harbor Lending Circle</span>
  </div>
  <p class="tagline">Borderless Mortgages.</p>
  <p class="cities--front">Singapore | Hong Kong | Shanghai | Manila</p>
  <div class="region-map" role="img" aria-label="Dotted map of Asia with office locations highlighted"></div>
</section>

<section class="card card--back" aria-label="Card back">
  <svg class="card__bg" viewBox="0 0 264 462" aria-hidden="true">
    <rect width="264" height="462" fill="var(--red)"/>
    <path d="M0,92 C70,40 180,18 264,48 L264,400 C180,425 80,420 0,395 Z" fill="var(--blue)"/>
    <path d="M26,96 C90,70 190,62 264,86 L264,404 C180,420 90,418 26,404 Z" fill="var(--white)"/>
    <path d="M0,84 L26,96 L26,404 L0,395 Z" fill="var(--black)"/>
    <rect x="26" y="169" width="238" height="38" fill="var(--blue-band)"/>
    <rect x="98" y="213" width="166" height="33" fill="var(--blue-band)"/>
    <rect x="13" y="217" width="48" height="171" fill="var(--red-bright)"/>
    <path d="M0,402 C80,420 180,420 264,396 L264,410 C180,432 80,432 0,414 Z" fill="var(--blue)" stroke="var(--white)" stroke-width="2"/>
    <path d="M0,416 C80,434 180,434 264,412 L264,462 L0,462 Z" fill="var(--red)"/>
  </svg>

  <div class="brand">
    <span class="brand__mark"></span>
    <span class="brand__name">Harbor Lending Circle</span>
  </div>

  <h1 class="person__name">Peter Wilks</h1>
  <p class="person__title">Co-Founder | Partner</p>

  <svg class="icon icon--phone" viewBox="0 0 24 24" aria-hidden="true">
    <path d="M6 3 L9 3 L10.5 7.5 L8.5 9.5 C9.5 12 12 14.5 14.5 15.5 L16.5 13.5 L21 15 L21 18 C21 19.5 19.5 21 18 21 C10 20.5 3.5 14 3 6 C3 4.5 4.5 3 6 3 Z" fill="none" stroke="var(--white)" stroke-width="1.6" stroke-linejoin="round"/>
  </svg>
  <p class="contact contact--phone">+65 555-0142</p>

  <svg class="icon icon--email" viewBox="0 0 24 24" aria-hidden="true">
    <rect x="2.5" y="5" width="19" height="14" fill="none" stroke="var(--white)" stroke-width="1.8"/>
    <path d="M2.5 5 L12 13 L21.5 5" fill="none" stroke="var(--white)" stroke-width="1.8"/>
  </svg>
  <p class="contact contact--email">peterwilks@hlc-example.asia</p>

  <svg class="icon icon--web" viewBox="0 0 24 24" aria-hidden="true">
    <g fill="none" stroke="var(--white)" stroke-width="1.5">
      <circle cx="12" cy="12" r="9.5"/>
      <ellipse cx="12" cy="12" rx="4.5" ry="9.5"/>
      <line x1="2.5" y1="12" x2="21.5" y2="12"/>
      <path d="M4 7 H20 M4 17 H20"/>
    </g>
  </svg>
  <p class="contact contact--web">www.hlc-example.asia</p>

  <svg class="icon icon--pin" viewBox="0 0 24 24" aria-hidden="true">
    <path d="M12 2 C7.5 2 4.5 5.3 4.5 9.3 C4.5 14.5 12 22 12 22 C12 22 19.5 14.5 19.5 9.3 C19.5 5.3 16.5 2 12 2 Z" fill="var(--white)"/>
    <circle cx="12" cy="9.3" r="3" fill="var(--red-bright)"/>
  </svg>
  <p class="contact contact--address">14 Cassia Lane, Suite 310<br>Singapore 047219</p>

  <div class="handle" aria-label="Messaging ID: peterwilks">
    <span class="handle__dot"></span>
    <span class="handle__id">peterwilks</span>
  </div>

  <p class="cities--back">Singapore | Hong Kong | Shanghai | Manila</p>
</section>

</body>
</html>
```